www.brevatin.com Sales/Order Page ReDesign

We need a new and amazing design for our sales/order page to attract more costumers and new houses for our portal.

Here is the existing page with the current design: https://www.brevatin.com/sales

We are proud owners of www.sommarhytta.no and www.brevatin.com and we want more holiday home owners to join our page so that we can rent out their holiday homes and increase the number of houses on our portal.

To get more homeowners we need a sales page that can sell our products the best way possible. Therefore we want you too blow us away with a fresh, modern, easy understandable and stylish new sales/order page.

The only restrictions we give when it comes to design is that it needs to fit the existing design of our portals, the top and footer are set. Beside that we are open for everything as long as it at once give the customers impression that this is a good, professional page were they just have to put out their houses.

When it comes to content I have added two documents who include the content to put in here and some guidelines on how to organize the page. Please be creative and add necessary graphics, symbols, background pictures and what ever necessary to make this page look professional and appealing to new costumers.

Looking forward to what suggestions we are given.

We just want to inform that we have updated our brief with a much more concrete description of what content to add on the sale page, and who to structure the content on the page. Hope this helps to make suggestions easier. Looking forward to receive some good contributions.

We would just like to make sure that everyone have understood that we are not asking for a new design suggestion to our portal in general. We are only asking for a redesign of our sales/order page you find here www.brevatin.com/sales. We have to day received some designs for our front page and the design it self was good, but that's not what we are asking for this time and don't want you to use time of something we don't need at the moment. We are looking forward too se some good suggestions.

Reason: Hello. Thanks for all the great contributions we have been given so fare. We haven't been able to respond to all design and are therefore extending the deadline so that we are able to respond to the designs we have been giver and to gov time to make final changes.

Reason: We are extending the deadline to give designers time to give new suggestion based on our latest feedback today.

Reason: Extended so we can receive last design changes.

Target Market(s)

This is a presentation page where we present our product agains new home owner who we what to choose listing there property on or site.

Industry/Entity Type

Sales

Requirements
Must have
• A modern design who calms the costumer down and help them in deciding to chose us, and for them to choose us they need to trust and believe in us. Therefore your main task is to create a page that effectively informs about our product, gets the visitors attentions and make them trust us.
Nice to have
• Examples of good competitors and good order pages we like:

http://www.cabinquest.example/info/lyp?icid=IL___O_Text___top_nav_link
https://www.nestlodge.example/rooms/new
https://www.pearvix.example/phone/compare/
http://www.guestnook.example/host
Should not have
• - Bad design :-). With bad design we mean design that looks like it's made in 2 seconds by a little child.

```html
<!DOCTYPE html>
<html lang="en">
<head>
<meta charset="utf-8">
<title>Brevatin – List your holiday home</title>
<link rel="stylesheet" href="https://fonts.googleapis.com/css2?family=Cinzel:wght@400;700&family=Open+Sans:wght@400;600;700&display=swap">
<style>
:root{
  --ink:#2b2e33;
  --muted:#9a9ea4;
  --blue:#0fa6e6;
  --blue-dark:#0a8dcc;
  --teal:#35c0cf;
  --header:#22252b;
  --band:#25282f;
  --footer:#1b1c1f;
  --line:#e6e7e9;
  --white:#ffffff;
  --orange:#e98a3c;
  --green:#5cbf8b;
  --yellow:#f0bf2f;
  --red:#e25a4f;
  --coral:#ee7b5c;
  --sea:#55b3ba;
}
*{box-sizing:border-box;margin:0;padding:0}
html,body{width:1200px;height:2632px;overflow:hidden}
body{position:relative;font-family:"Open Sans",Arial,sans-serif;color:var(--ink);background:var(--white)}
.abs{position:absolute}
.serif{font-family:"Cinzel",Georgia,serif}

/* header */
.site-header{left:0;top:0;width:1200px;height:93px;background:var(--header)}
.brand{left:175px;top:26px;display:flex;align-items:center;gap:12px}
.brand-mark{width:38px;height:38px;background:var(--blue);border-radius:4px}
.brand-name{font-family:"Cinzel",Georgia,serif;font-size:30px;color:var(--white);font-weight:400;letter-spacing:1px}
.main-nav a{position:absolute;top:38px;color:var(--white);font-size:15px;text-decoration:none}
.signup{left:931px;top:40px;width:92px;height:23px;background:var(--blue);color:var(--white);font-size:11px;font-weight:700;text-align:center;line-height:23px}

/* hero */
.hero{left:0;top:93px;width:1200px;height:495px;background:linear-gradient(160deg,#3c5d8c 0%,#1d3556 40%,#2a2520 65%,#7a4f22 85%,#d39243 100%)}
.hero-welcome{left:179px;top:195px;color:var(--white);font-size:29px;letter-spacing:1px}
.hero-welcome .serif{font-size:52px}
.hero-sub{left:179px;top:248px;color:var(--white);font-size:25px}
.hero-title{left:179px;top:318px;color:var(--white);font-family:"Cinzel",Georgia,serif;font-size:44px;line-height:56px;letter-spacing:1px}

/* search */
.search-bar{left:0;top:588px;width:1200px;height:80px;background:#ececec}
.field{top:24px;height:34px;background:var(--white);border:1px solid #d3d3d3;font-size:10px;font-style:italic;color:#666;padding:10px 8px}
.field.select::after{content:"";position:absolute;right:0;top:0;width:24px;height:32px;border-left:1px solid #d3d3d3;background:linear-gradient(#fafafa,#e9e9e9)}
.field.select::before{content:"";position:absolute;right:7px;top:13px;border:5px solid transparent;border-top:7px solid #333;z-index:1}
.search-btn{left:884px;top:24px;width:139px;height:34px;background:linear-gradient(var(--teal),var(--blue-dark));color:var(--white);font-weight:700;font-size:13px;text-align:center;line-height:34px}

/* features */
.feature-icon{width:70px;height:70px;background:var(--blue)}
.feature h3{font-family:"Cinzel",Georgia,serif;font-weight:400;font-size:16px;color:#3a3d42;letter-spacing:.5px;line-height:18px}
.feature p{font-size:11px;color:var(--muted);line-height:19px;margin-top:6px;width:240px}
.feature a{display:block;font-size:12px;color:var(--blue-dark);margin-top:6px;text-decoration:none}
.rule-v{width:1px;background:var(--line)}
.rule-h{height:1px;background:var(--line)}

/* contact band */
.contact-band{left:0;top:1110px;width:1200px;height:364px;background:linear-gradient(#2c2f36,#1f2227)}
.photo-circle{left:216px;top:1144px;width:228px;height:228px;border-radius:50%;border:6px solid var(--white);background:linear-gradient(135deg,#cfd6de,#6f7c8c 60%,#2b3340)}
.info-circle{left:408px;top:1212px;width:218px;height:218px;border-radius:50%;border:6px solid var(--white);background:#202328;color:var(--white);text-align:center;padding:36px 14px 0;overflow:hidden}
.info-circle h4{font-family:"Cinzel",Georgia,serif;font-weight:400;color:var(--teal);font-size:12.5px;line-height:16px}
.info-circle p{font-size:10px;line-height:16px;margin-top:8px;white-space:nowrap}
.contact-copy{left:716px;top:1192px;color:var(--white)}
.contact-copy h2{font-family:"Cinzel",Georgia,serif;font-weight:400;font-size:21px;line-height:26px;letter-spacing:.5px}
.contact-copy .phone{font-family:"Cinzel",Georgia,serif;color:var(--teal);font-size:20px;margin-top:20px}
.contact-copy .mail{font-size:13px;margin-top:4px}
.contact-copy .hours{font-family:"Cinzel",Georgia,serif;font-size:14px;line-height:22px;margin-top:18px}

/* services */
.services-title{left:0;top:1534px;width:1200px;text-align:center;font-family:"Cinzel",Georgia,serif;font-size:31px;color:#2b2e33;letter-spacing:1px}
.services-sub{left:0;top:1588px;width:1200px;text-align:center;font-size:11.5px;color:#6d7075}
.services-underline{left:320px;top:1626px;width:560px;height:1px;background:linear-gradient(90deg,transparent,#cfd1d4,transparent)}
.service-icon{width:64px;height:64px;border-radius:50%}
.service h3{font-family:"Cinzel",Georgia,serif;font-weight:700;font-size:15px;color:#2b2e33;letter-spacing:.5px}
.service p{font-size:11px;color:#6d7075;line-height:18px;margin-top:4px;width:300px}
.view-more{display:inline-block;margin-top:8px;border:1px solid #c9c9c9;font-size:8.5px;font-weight:700;color:#555;padding:3px 10px;letter-spacing:.3px}
.view-more.active{background:var(--blue);border-color:var(--blue);color:var(--white)}

/* footer */
.site-footer{left:0;top:2175px;width:1200px;height:457px;background:linear-gradient(160deg,#232427,#161719)}
.footer-title{left:0;top:2210px;width:1200px;text-align:center;color:var(--white);font-size:30px;letter-spacing:1px}
.footer-tag{left:0;top:2266px;width:1200px;text-align:center;color:#e6e6e6;font-size:13px}
.footer-col h5{font-family:"Cinzel",Georgia,serif;font-weight:400;color:var(--white);font-size:17px;letter-spacing:.5px}
.footer-col ul{list-style:none;margin-top:10px}
.footer-col li{font-size:11.5px;color:#c9c9c9;line-height:22px}
.footer-col li::before{content:"•";margin-right:8px;color:#888}
.map{left:637px;top:2359px;width:175px;height:118px;background:linear-gradient(135deg,#e9e6dd,#d8d3c6);border:3px solid #eee}
.contact-info{left:835px;top:2358px;color:var(--white)}
.contact-info h5{font-size:17px;font-weight:400;letter-spacing:.5px}
.contact-info .row{display:flex;gap:10px;margin-top:12px;font-size:11.5px;line-height:16px;color:#ddd}
.contact-info .row.big{font-size:15px;color:var(--white)}
.contact-info svg{flex:none;margin-top:2px}
.copyright{left:181px;top:2584px;font-size:9.5px;color:#ccc}
.social{top:2587px;width:24px;height:24px;border:1px solid #bbb;border-radius:50%}
</style>
</head>
<body>

<header class="abs site-header">
  <div class="abs brand"><span class="brand-mark"></span><span class="brand-name">Brevatin</span></div>
  <nav class="main-nav">
    <a style="left:446px">Home</a>
    <a style="left:517px">Rooms</a>
    <a style="left:593px">Amenities</a>
    <a style="left:688px">Services</a>
    <a style="left:772px">Pages</a>
    <a style="left:843px">Location</a>
  </nav>
  <div class="abs signup">SIGN UP</div>
</header>

<section class="abs hero" role="img" aria-label="Evening photo of an overwater resort deck with lanterns and lounge chairs by the sea"></section>
<div class="abs hero-welcome">WELCOME TO <span class="serif">BREVATIN</span></div>
<div class="abs hero-sub">AT ITS HEAVENLY BEST</div>
<h1 class="abs hero-title" style="font-weight:400">FIND A<br>PLACE TO STAY</h1>

<section class="abs search-bar">
  <div class="abs field" style="left:177px;width:230px">Country, Region, City, Property ID</div>
  <div class="abs field select" style="left:419px;width:139px">Arrival</div>
  <div class="abs field select" style="left:572px;width:138px">Departure</div>
  <div class="abs field select" style="left:723px;width:140px">Length of Holiday</div>
  <div class="abs search-btn">SEARCH</div>
</section>

<section class="features">
  <div class="abs rule-v" style="left:598px;top:740px;height:322px"></div>
  <div class="abs rule-h" style="left:290px;top:895px;width:660px"></div>

  <div class="abs feature-icon" style="left:210px;top:767px">
    <svg width="70" height="70" viewBox="0 0 70 70"><circle cx="35" cy="35" r="18" fill="none" stroke="#fff" stroke-width="2.5"/><ellipse cx="35" cy="35" rx="8" ry="18" fill="none" stroke="#fff" stroke-width="2"/><line x1="17" y1="35" x2="53" y2="35" stroke="#fff" stroke-width="2"/></svg>
  </div>
  <div class="abs feature" style="left:326px;top:768px">
    <h3>Good exposure</h3>
    <p>List across TripRoamer's 23 international<br>websites at no extra cost and build your<br>reputation through reviews</p>
    <a>Read more</a>
  </div>

  <div class="abs feature-icon" style="left:651px;top:767px">
    <svg width="70" height="70" viewBox="0 0 70 70"><rect x="22" y="20" width="26" height="30" rx="3" fill="none" stroke="#fff" stroke-width="2.5" transform="rotate(-20 35 35)"/><line x1="24" y1="30" x2="46" y2="22" stroke="#fff" stroke-width="3"/></svg>
  </div>
  <div class="abs feature" style="left:768px;top:768px">
    <h3>Secure online booking</h3>
    <p>Tenants expect to be able to pay online; we<br>give you the ability to easily and safe charge<br>your costumers to be even more comple-</p>
    <a>Read more</a>
  </div>

  <div class="abs feature-icon" style="left:210px;top:942px">
    <svg width="70" height="70" viewBox="0 0 70 70"><circle cx="35" cy="35" r="17" fill="none" stroke="#fff" stroke-width="2.5" stroke-dasharray="2 4"/><circle cx="35" cy="35" r="11" fill="none" stroke="#fff" stroke-width="1.5" stroke-dasharray="2 3"/></svg>
  </div>
  <div class="abs feature" style="left:326px;top:940px">
    <h3>Flexible payment plans</h3>
    <p>Whether you prefer to pay commission,<br>pay-per-lead or set up a monthly subscrip-<br>tion we have the solution. Together we will</p>
    <a>Read more</a>
  </div>

  <div class="abs feature-icon" style="left:651px;top:942px">
    <svg width="70" height="70" viewBox="0 0 70 70"><path d="M22 44h26a8 8 0 0 0 0-16 11 11 0 0 0-21-2 9 9 0 0 0-5 18z" fill="none" stroke="#fff" stroke-width="2.5"/></svg>
  </div>
  <div class="abs feature" style="left:768px;top:940px">
    <h3>Easy to get started &amp;<br>updated</h3>
    <p>We can integrate your listings with an XML<br>feed, your website or your favorite software</p>
    <a>Read more</a>
  </div>
</section>

<section class="abs contact-band"></section>
<div class="abs photo-circle" role="img" aria-label="Photo of smiling account managers wearing headsets"></div>
<div class="abs info-circle">
  <h4>Dedicated account<br>managers</h4>
  <p>Our multilingual team are experts<br>on marketing holiday lettings<br>around the world. Your personal<br>account manager will help you get<br>the biggest return on investment<br>for your portfolio.</p>
</div>
<div class="abs contact-copy">
  <h2>Contact us if you need<br>help to list</h2>
  <div class="phone">+47 41 20 58 37</div>
  <div class="mail">propertymanagers@brevatin.com</div>
  <div class="hours">Monday to Friday<br>from 09:00 to 17:30<br>Closed Saturdays and Sundays</div>
</div>

<h2 class="abs services-title" style="font-weight:400">Our services</h2>
<p class="abs services-sub">let's take a look at our modules Out of the box communication solutions to prospect.</p>
<div class="abs services-underline"></div>

<div class="abs rule-v" style="left:596px;top:1695px;height:410px"></div>
<div class="abs rule-h" style="left:210px;top:1819px;width:781px"></div>
<div class="abs rule-h" style="left:210px;top:1975px;width:781px"></div>

<div class="abs service-icon" style="left:210px;top:1697px;background:var(--orange)"><svg width="64" height="64"><circle cx="32" cy="32" r="12" fill="none" stroke="#fff" stroke-width="2.5"/><path d="M32 24v8l5 4" stroke="#fff" stroke-width="2.5" fill="none"/></svg></div>
<div class="abs service" style="left:289px;top:1696px"><h3>Access Scandinavians</h3><p>Our roots are from Norway, and we know the<br>Scandinavian market especially good and help you<br>get tenants from these very travel friendly markets.</p><span class="view-more">VIEW MORE ▸</span></div>

<div class="abs service-icon" style="left:628px;top:1697px;background:var(--green)"><svg width="64" height="64"><circle cx="32" cy="26" r="7" fill="#fff"/><path d="M19 46a13 11 0 0 1 26 0z" fill="#fff"/></svg></div>
<div class="abs service" style="left:707px;top:1696px"><h3>Broad exposure</h3><p>We have been in the market for several years and<br>are promoting your property true the necessary and<br>right channels.</p><span class="view-more">VIEW MORE ▸</span></div>

<div class="abs service-icon" style="left:210px;top:1854px;background:var(--yellow)"><svg width="64" height="64"><path d="M32 18l12 5v9c0 8-6 12-12 14-6-2-12-6-12-14v-9z" fill="#fff"/><path d="M26 32l4 4 8-8" stroke="var(--yellow)" stroke-width="2.5" fill="none"/></svg></div>
<div class="abs service" style="left:289px;top:1852px"><h3>Trust &amp; Safety</h3><p>You are still in control of your property. We have<br>good tools who help you accept a booking only if<br>you're 100% comfortable.</p><span class="view-more active">VIEW MORE ▸</span></div>

<div class="abs service-icon" style="left:628px;top:1854px;background:var(--red)"><svg width="64" height="64"><rect x="20" y="22" width="24" height="22" rx="2" fill="none" stroke="#fff" stroke-width="2.5"/><line x1="20" y1="29" x2="44" y2="29" stroke="#fff" stroke-width="2.5"/><text x="32" y="41" font-size="9" fill="#fff" text-anchor="middle" font-family="Open Sans,sans-serif">16</text></svg></div>
<div class="abs service" style="left:707px;top:1852px"><h3>No Traveler fees</h3><p>Unlike many other vacation rental booking site,<br>travelers can book vacation rentals without paying<br>any fees to us, maybe one of the reason</p><span class="view-more">VIEW MORE ▸</span></div>

<div class="abs service-icon" style="left:210px;top:2007px;background:var(--coral)"><svg width="64" height="64"><rect x="19" y="22" width="26" height="20" rx="2" fill="none" stroke="#fff" stroke-width="2.5"/><line x1="19" y1="28" x2="45" y2="28" stroke="#fff" stroke-width="3"/></svg></div>
<div class="abs service" style="left:289px;top:2006px"><h3>Payments by Brevatin</h3><p>Guests are always carful when it comes to payment.<br>Lets everybody feel safe true secure payment with<br>Brevatin. Then we are responsible that you get paid.</p><span class="view-more">VIEW MORE ▸</span></div>

<div class="abs service-icon" style="left:628px;top:2007px;background:var(--sea)"><svg width="64" height="64"><rect x="23" y="20" width="18" height="24" rx="2" fill="#fff"/><text x="32" y="37" font-size="13" fill="var(--sea)" text-anchor="middle" font-family="Open Sans,sans-serif" font-weight="700">$</text></svg></div>
<div class="abs service" style="left:707px;top:2006px"><h3>Online Booking</h3><p>We simplifies the booking process by allowing<br>tenants to send online reservations request which<br>gives you a 24-hour period to accept or</p><span class="view-more">VIEW MORE ▸</span></div>

<footer class="abs site-footer"></footer>
<h2 class="abs footer-title" style="font-weight:400">GET IN TOUCH</h2>
<p class="abs footer-tag">The week program designed to improve your everyday life. It will focus on mobility,&nbsp; flexibility, core strength</p>

<div class="abs footer-col" style="left:179px;top:2318px"><h5>Destinations</h5>
  <ul><li>Blog</li><li>Staff</li><li>Testimonials</li><li>Referral program</li><li>Spa membership</li><li>Gift certificates</li><li>Leave feedback</li></ul></div>
<div class="abs footer-col" style="left:368px;top:2318px"><h5>Services</h5>
  <ul><li>Northan Virginia</li><li>Annandale</li><li>Fairfax</li><li>Fair oaks</li><li>Alexandria</li><li>Mclean</li><li>Tysons&nbsp; Corner</li><li>Centervilla</li></ul></div>
<div class="abs footer-col" style="left:495px;top:2318px"><h5>&nbsp;</h5>
  <ul><li>Vienna Arlington</li><li>Herndon</li><li>Reston</li><li>Loudon</li><li>Lansdowne</li><li>Dulles</li><li>Sterling</li><li>Leesburg</li></ul></div>
<div class="abs footer-col" style="left:638px;top:2318px"><h5>Contact&nbsp; us</h5></div>
<div class="abs map" role="img" aria-label="Small street map showing the office location"></div>

<div class="abs contact-info">
  <h5>CONTACT INFO</h5>
  <div class="row"><svg width="10" height="14" viewBox="0 0 10 14"><path d="M5 0a5 5 0 0 0-5 5c0 4 5 9 5 9s5-5 5-9a5 5 0 0 0-5-5z" fill="#fff"/><circle cx="5" cy="5" r="2" fill="#1b1c1f"/></svg><span>BREVATIN HOLIDAY RENTAL<br>4410 Maple Hollow Rd. Vienna,<br>VA 22180</span></div>
  <div class="row big"><svg width="13" height="13" viewBox="0 0 13 13"><path d="M3 0l2 3-1.5 1.5a8 8 0 0 0 5 5L10 8l3 2-1.5 3C6 13 0 7 0 1.5z" fill="#fff"/></svg><span>(703) 555-0148</span></div>
  <div class="row"><svg width="13" height="10" viewBox="0 0 13 10"><rect width="13" height="10" rx="1" fill="#fff"/><path d="M0 1l6.5 5L13 1" stroke="#1b1c1f" fill="none"/></svg><span style="font-size:13px;color:#fff">info@brevatin-stays.com</span></div>
</div>

<p class="abs copyright">Copyright LINDQVIST STUDIO © 2014. All rights reserved. Terms and Conditions</p>
<div class="abs social" style="left:904px"></div>
<div class="abs social" style="left:933px;border-color:var(--blue)"></div>
<div class="abs social" style="left:962px"></div>
<div class="abs social" style="left:991px"></div>

</body>
</html>
```